Brochure and Price List
Quiet Willow Body & Beauty Therapies
Because of a problem on their end that delayed the veiling of this project Pexalune has extended my project by 2 days.
Although there are some designers who have withheld their designs because of the veiling problem I don't expect I will need that full amount of time to choose a winner.
I would like to state again that my preference is for a square brochure in booklet form and a price list in rectangular form listing all the treatments with their prices on the front and all the policies on the back. There will be no treatment descriptions required in the booklet.
I will review and respond to every design.
Thank you!
Here are the omitted business details:
Business Name: Quiet Willow Body & Beauty Therapies
My Name and Qualifications: Marisol T. Dunbeck Dip. Massage & Beauty Therapy
Business Telephone: 441-356-8120
Email: roamingrestmd@fernpost.example
Website: www.quietwillowmobile.example
Tag-lines: Island-wide in-home spa treatments
Call today for bookings
Just a query about the folded brochure vs booklet form:
Is the booklet format a really difficult style to pull off? I noticed that no-one has submitted any booklet or separate price list as of yet and I wonder if it's not the best idea for the look I'm going for. Your creative opinions are welcome.
Thanks!
Hello folks!
The administrators were unable to add the information I sent them to the brief. This is one more effort to get the information to you in the form of a Word document. Please view the attached document for further details of the price list and brochure.
Marisol
I see that #11 is using the same tagline as #1; however, since my own script will be used in the final outcome I do not expect that to be an issue. I regard it only as a filler to demonstrate the use of the space. I have asked for the project to be veiled so that designers cannot see each other's work. That should make you all more comfortable.
I have sent more details to the support team for them to add to my brief. Hopefully that will be posted today.
***Please note that I love the look of "dots" stretching between the treatment item and price on the price list.***
For example:
Hot Stones Pedicure.............................................$60
I would love to see the brochure in thin booklet form. This could be a square or rectangle oriented in landscape or portrait position.
I am very taken by the use of rich colour backgrounds in all these designs. They are beautiful. Thank you for thinking to add flowers and water. I love on a semi tropical island, so that depiction is a very accurate impression for my clients.
I will be checking back between massage appointments. Since I don't work behind a desk I don't have access to a computer while I am with a client.
Thanks again for your patience everyone!
Ohhh!!! Are you asking for the actual details of what will be written in the brochure? I'm sorry! I can add that in about 8 hours. I won't have another chance to get to the computer until then. I was mistaken about what the design stage would include. So sorry!
I put up 6 versions of the logo in the brief. Unfortunately, although I have seen some beautiful examples online, I do not own photos of bamboo and stones to show you what I like. I have downloaded some that I do not think would be allowed. That's the difficulty I am having.
where we can find the details for this project...so that i can start designing it..

```html
<!DOCTYPE html>
<html lang="en">
<head>
<meta charset="utf-8">
<title>Quiet Willow Body &amp; Beauty Therapies — Brochure and Price List</title>
<link href="https://fonts.googleapis.com/css2?family=Tinos:ital,wght@0,400;0,700;1,400&family=Great+Vibes&display=swap" rel="stylesheet">
<style>
  :root{
    --bg:#e4e4df;
    --paper:#ffffff;
    --ink:#151515;
    --muted:#555555;
    --black:#0b0b0b;
    --grey:#8d8d8d;
    --grey-light:#c9c9c9;
    --petal:#f1d949;
    --petal-deep:#c9a21c;
    --water:#22343a;
  }
  *{box-sizing:border-box;margin:0;padding:0}
  html,body{width:1200px;height:871px;overflow:hidden}
  body{background:var(--bg);font-family:"Tinos","Times New Roman",serif;color:var(--ink);position:relative}

  .page{position:absolute;width:380px;height:400px;background:var(--paper);overflow:hidden;box-shadow:0 1px 4px rgba(0,0,0,.25)}
  .page--dark{background:var(--black);color:#fff}

  .spread-cover .policies{left:40px;top:30px}
  .spread-cover .cover{left:420px;top:30px}
  .price-sheet{left:840px;top:30px;width:320px}
  .spread-inner .menu-left{left:40px;top:450px}
  .spread-inner .menu-right{left:420px;top:450px}
  .back-cover{left:840px;top:450px;width:320px}

  .script{font-family:"Great Vibes",cursive;font-weight:400}
  h2.script{font-size:26px;text-align:center;line-height:1.1;margin-bottom:4px}
  h3.script{font-size:19px;text-align:center;line-height:1.1;margin:6px 0 3px}
  .copy{font-size:8.5px;line-height:1.35;text-align:center;margin-bottom:4px}
  .copy--left{text-align:left}

  .list{font-size:8.5px;line-height:1.45}
  .row{display:flex;align-items:baseline}
  .row .dots{flex:1;border-bottom:1px dotted var(--ink);margin:0 3px;transform:translateY(-2px)}
  .hours{width:150px;margin:0 auto}

  .body{position:absolute;inset:0;padding:20px 30px}

  .band{position:absolute;left:0;right:0;bottom:0;height:70px}

  .brand{display:flex;align-items:center;gap:8px;position:absolute;left:24px;top:22px;font-size:15px;color:#fff}
  .brand-dot{width:14px;height:14px;border-radius:50%;background:#fff}
  .cover-photo{position:absolute;left:24px;top:70px;width:332px;height:170px;
    background:radial-gradient(ellipse at 40% 55%,var(--petal) 0,var(--petal-deep) 28%,var(--water) 62%,#0d1416 100%)}
  .cover .tagline{position:absolute;left:24px;right:24px;top:252px;font-size:24px;text-align:center;line-height:1.15}
  .cover .contact{position:absolute;left:0;right:0;bottom:26px;text-align:center;font-size:9px;line-height:1.5;color:#d6d6d6}

  .side-strip{position:absolute;top:0;bottom:0;width:38px;
    background:linear-gradient(180deg,var(--black) 0,#3b3b3b 45%,var(--black) 100%)}
  .price-sheet .side-strip{right:0;top:150px;bottom:90px}
  .price-sheet .body{right:48px;padding:16px 22px}

  .menu-right .side-strip{left:0}
  .menu-right .body{left:38px;padding:16px 22px}
  .portrait{float:right;width:96px;height:110px;margin:2px 0 4px 8px;
    background:linear-gradient(160deg,#efe3d8 0,#d7b49a 55%,#b88c70 100%)}

  .back-top{position:absolute;left:0;right:0;top:0;height:130px;background:var(--black)}
  .back-top .brand{top:16px;left:20px;font-size:13px}
  .back-photo{position:absolute;left:20px;right:20px;top:46px;height:74px;
    background:radial-gradient(ellipse at 50% 50%,var(--petal) 0,var(--petal-deep) 30%,var(--water) 75%)}
  .back-cover .body{top:134px;padding:8px 26px}
  .sign-off{margin-top:6px}
</style>
</head>
<body>

<section class="spread-cover">
  <article class="page policies">
    <div class="body">
      <h2 class="script">Policies</h2>
      <p class="copy">Please allow fifteen minutes for a consultation before your first treatment. Kindly inform your therapist of any health conditions, allergies or medication.</p>
      <p class="copy">Mobile visits require a quiet space near a power outlet. Travel outside the parish may carry a small fee.</p>
      <h3 class="script">Opening Hours</h3>
      <div class="list hours">
        <div class="row"><span>Monday</span><span class="dots"></span><span>9am – 6pm</span></div>
        <div class="row"><span>Tuesday</span><span class="dots"></span><span>9am – 6pm</span></div>
        <div class="row"><span>Wednesday</span><span class="dots"></span><span>9am – 6pm</span></div>
        <div class="row"><span>Thursday</span><span class="dots"></span><span>9am – 8pm</span></div>
        <div class="row"><span>Friday</span><span class="dots"></span><span>9am – 8pm</span></div>
        <div class="row"><span>Saturday</span><span class="dots"></span><span>10am – 4pm</span></div>
        <div class="row"><span>Sunday</span><span class="dots"></span><span>Closed</span></div>
      </div>
      <h3 class="script">Cancellations</h3>
      <p class="copy">A 24-hour notice is required to cancel or move a booking. Missed appointments are charged at half the treatment price. Late arrivals will receive the remaining time.</p>
      <p class="copy">Many Thanks</p>
    </div>
    <svg class="band" viewBox="0 0 380 70" preserveAspectRatio="none" aria-hidden="true">
      <path d="M0 30 C120 10 240 60 380 20 L380 70 L0 70 Z" fill="#0b0b0b"/>
      <path d="M0 30 C120 10 240 60 380 20 L380 28 C240 68 120 18 0 38 Z" fill="#9a9a9a"/>
    </svg>
  </article>

  <article class="page page--dark cover">
    <div class="brand"><span class="brand-dot"></span><span>Quiet Willow</span></div>
    <div class="cover-photo" role="img" aria-label="Yellow frangipani flowers floating in a dark bowl of water"></div>
    <p class="tagline script">Island-wide in-home spa treatments</p>
    <div class="contact">
      <p>Quiet Willow Body &amp; Beauty Therapies</p>
      <p>Marisol T. Dunbeck, Dip. Massage &amp; Beauty Therapy</p>
      <p>441-356-8120</p>
      <p>roamingrestmd@fernpost.example</p>
      <p>www.quietwillowmobile.example</p>
    </div>
  </article>
</section>

<article class="page price-sheet">
  <div class="body">
    <h2 class="script">For the Body</h2>
    <div class="list">
      <div class="row"><span>Swedish Massage 60 min</span><span class="dots"></span><span>$85</span></div>
      <div class="row"><span>Swedish Massage 90 min</span><span class="dots"></span><span>$115</span></div>
      <div class="row"><span>Deep Tissue Massage</span><span class="dots"></span><span>$95</span></div>
      <div class="row"><span>Hot Stone Massage</span><span class="dots"></span><span>$110</span></div>
      <div class="row"><span>Aromatherapy Massage</span><span class="dots"></span><span>$90</span></div>
      <div class="row"><span>Back, Neck &amp; Shoulders</span><span class="dots"></span><span>$55</span></div>
      <div class="row"><span>Pregnancy Massage</span><span class="dots"></span><span>$85</span></div>
      <div class="row"><span>Sea Salt Body Scrub</span><span class="dots"></span><span>$70</span></div>
      <div class="row"><span>Seaweed Body Wrap</span><span class="dots"></span><span>$90</span></div>
      <div class="row"><span>Reflexology Session</span><span class="dots"></span><span>$60</span></div>
    </div>
    <h3 class="script">Soothing Waxing</h3>
    <div class="list">
      <div class="row"><span>Eyebrow Shape</span><span class="dots"></span><span>$15</span></div>
      <div class="row"><span>Lip or Chin</span><span class="dots"></span><span>$12</span></div>
      <div class="row"><span>Underarm</span><span class="dots"></span><span>$20</span></div>
      <div class="row"><span>Half Leg</span><span class="dots"></span><span>$35</span></div>
      <div class="row"><span>Full Leg</span><span class="dots"></span><span>$55</span></div>
      <div class="row"><span>Bikini Line</span><span class="dots"></span><span>$30</span></div>
    </div>
    <h3 class="script">Tinting</h3>
    <div class="list">
      <div class="row"><span>Brow Tint</span><span class="dots"></span><span>$15</span></div>
      <div class="row"><span>Lash Tint</span><span class="dots"></span><span>$20</span></div>
    </div>
    <h3 class="script">In the Hands and Feet</h3>
    <div class="list">
      <div class="row"><span>Classic Manicure</span><span class="dots"></span><span>$35</span></div>
      <div class="row"><span>Hot Stones Pedicure</span><span class="dots"></span><span>$60</span></div>
    </div>
  </div>
  <div class="side-strip" role="img" aria-label="Black strip with pale bamboo stems"></div>
</article>

<section class="spread-inner">
  <article class="page menu-left">
    <div class="body">
      <p class="copy copy--left">Every treatment is brought to your door with fresh linens, warm oils and calm music, so you can rest in comfort without leaving home.</p>
      <div class="list">
        <div class="row"><span>Express Facial</span><span class="dots"></span><span>$50</span></div>
        <div class="row"><span>Classic Cleansing Facial</span><span class="dots"></span><span>$70</span></div>
        <div class="row"><span>Hydrating Facial</span><span class="dots"></span><span>$80</span></div>
        <div class="row"><span>Anti-Ageing Facial</span><span class="dots"></span><span>$95</span></div>
        <div class="row"><span>Teen Clear Skin Facial</span><span class="dots"></span><span>$55</span></div>
        <div class="row"><span>Back Cleanse</span><span class="dots"></span><span>$65</span></div>
        <div class="row"><span>Eye Revive Treatment</span><span class="dots"></span><span>$40</span></div>
        <div class="row"><span>Scalp Massage</span><span class="dots"></span><span>$35</span></div>
        <div class="row"><span>Hand &amp; Arm Massage</span><span class="dots"></span><span>$30</span></div>
        <div class="row"><span>Foot Ritual</span><span class="dots"></span><span>$40</span></div>
        <div class="row"><span>Couples Massage</span><span class="dots"></span><span>$170</span></div>
        <div class="row"><span>Spa Day Package</span><span class="dots"></span><span>$210</span></div>
      </div>
      <h3 class="script">Soothing Waxing</h3>
      <p class="copy">Gentle warm wax suited to sensitive skin, finished with a cooling aloe balm.</p>
      <div class="list">
        <div class="row"><span>Full Arm</span><span class="dots"></span><span>$35</span></div>
        <div class="row"><span>Half Arm</span><span class="dots"></span><span>$25</span></div>
        <div class="row"><span>Back</span><span class="dots"></span><span>$45</span></div>
        <div class="row"><span>Chest</span><span class="dots"></span><span>$40</span></div>
        <div class="row"><span>Full Face</span><span class="dots"></span><span>$35</span></div>
      </div>
    </div>
  </article>

  <article class="page menu-right">
    <div class="side-strip" role="img" aria-label="Black strip with pale bamboo stems"></div>
    <div class="body">
      <h3 class="script">Tinting</h3>
      <div class="list">
        <div class="row"><span>Brow Tint</span><span class="dots"></span><span>$15</span></div>
        <div class="row"><span>Lash Tint</span><span class="dots"></span><span>$20</span></div>
        <div class="row"><span>Brow &amp; Lash</span><span class="dots"></span><span>$30</span></div>
      </div>
      <h3 class="script">In the Hands and Feet</h3>
      <p class="copy">Soak, shape and polish in the calm of your own home, with a warm towel wrap and a slow relaxing massage for tired hands and feet.</p>
      <div class="list">
        <div class="row"><span>Classic Manicure</span><span class="dots"></span><span>$35</span></div>
        <div class="row"><span>Spa Manicure</span><span class="dots"></span><span>$45</span></div>
        <div class="row"><span>Classic Pedicure</span><span class="dots"></span><span>$45</span></div>
        <div class="row"><span>Hot Stones Pedicure</span><span class="dots"></span><span>$60</span></div>
        <div class="row"><span>Polish Change</span><span class="dots"></span><span>$15</span></div>
      </div>
      <h3 class="script">Making Relaxation Opportunities</h3>
      <div class="portrait" role="img" aria-label="Photo of a woman relaxing during a spa treatment"></div>
      <p class="copy copy--left">Gift vouchers are available for every treatment and package. Group bookings for bridal parties, birthdays and retreats can be arranged on request. Call today for bookings and let us bring the spa to you.</p>
    </div>
  </article>
</section>

<article class="page back-cover">
  <div class="back-top">
    <div class="brand"><span class="brand-dot"></span><span>Quiet Willow</span></div>
    <div class="back-photo" role="img" aria-label="Yellow frangipani flowers on dark water"></div>
  </div>
  <div class="body">
    <h3 class="script">About</h3>
    <p class="copy">Quiet Willow offers island-wide in-home spa treatments by a fully qualified therapist, bringing calm, care and comfort to your home, hotel or villa.</p>
    <h3 class="script">Cancellations</h3>
    <p class="copy">Please give 24 hours notice to cancel. Missed visits are charged at half price.</p>
    <h3 class="script">Opening Hours</h3>
    <div class="list hours">
      <div class="row"><span>Mon – Wed</span><span class="dots"></span><span>9am – 6pm</span></div>
      <div class="row"><span>Thu – Fri</span><span class="dots"></span><span>9am – 8pm</span></div>
      <div class="row"><span>Saturday</span><span class="dots"></span><span>10am – 4pm</span></div>
      <div class="row"><span>Sunday</span><span class="dots"></span><span>Closed</span></div>
    </div>
    <p class="copy sign-off">Many Thanks</p>
  </div>
</article>

</body>
</html>
```